Web Design Project

We are a SaaS company that specializes in the thrift industry POS and inventory software. We want a clean and professional site that does NOT look like a template site.

*** A little more about our business -
We offer a SaaS (Software As A Service) for a Point Of Sale and inventory control product specifically for the Thrift / Second hand industry. The software allows them to process inventory, grade/rate it, create the barcoded tags. It the does the whole retail sale process. We also offer tie-ins to Plumora, Zentiq and pebble/vorn mobile apps to support our customers thrift stores.

We need to in incorporate the look/feel and color scheme of our logo.

I would imagine possibly a HTML5 slideshow (3-5 slides) rotating on the home page showing screenshots, etc.

I am envisioning icons representing features of our product.

PLEASE ask questions, I am sure I have left out a ton.

Reason: I am increasing the budget.

Reason: I have had a harder time with content than I thought I would.

Reason: I was very ill, but I am back and want to get it finished up!

Requirements
Must have
• I have attached a couple of our logo's with color options. It needs to flow with that.

I have also attached a screen shot of what I think might work. This DOESN'T suggest that is what I am looking for, just a sample.

I am thinking a home page and maybe one or two sub pages
***Update, I kind of like the following concept for one of the sub-pages
http://www.quelbrix.example/estimate.html

There should also be a place to highlight Plumora and zentiq.

It will be a bilingual / multilingual site, so take that into account
Should not have
• I don't want it to look like a template site. It should be clean and professional.

```html
<!DOCTYPE html>
<html lang="en">
<head>
<meta charset="utf-8">
<title>Resale Bright – Online Point-of-Sale Solution</title>
<link rel="stylesheet" href="https://fonts.googleapis.com/css2?family=Roboto+Condensed:wght@400;700&family=Arimo:wght@400;700&display=swap">
<style>
:root{
  --sky:#00aeef;
  --sky-deep:#0096d6;
  --sky-light:#3fc4f5;
  --ink:#3a3a3a;
  --text:#555;
  --muted:#666;
  --panel-dark:#2b2b2b;
  --footer:#1e1e1e;
  --footer-panel:#262626;
  --footer-line:#111;
  --green:#5fbf16;
  --green-dark:#3f9a07;
  --white:#fff;
  --circle:#ececec;
}
*{margin:0;padding:0;box-sizing:border-box}
html,body{width:966px;height:1200px;overflow:hidden;background:var(--footer)}
body{font-family:"Arimo",Arial,sans-serif;position:relative}
.page{position:relative;width:966px;height:1200px;overflow:hidden}

/* header */
.site-header{position:absolute;top:0;left:0;width:966px;height:84px;background:linear-gradient(#f6f6f6,#e2e2e2);border-bottom:1px solid #d0d0d0}
.brand{position:absolute;left:24px;top:22px;display:flex;align-items:center;gap:10px}
.brand-mark{width:30px;height:30px;background:var(--sky-deep);border-radius:4px}
.brand-name{font-family:"Roboto Condensed",sans-serif;font-weight:700;font-size:30px;color:var(--sky-deep);letter-spacing:.5px}
.main-nav{position:absolute;top:26px;right:14px;display:flex;font-family:"Roboto Condensed",sans-serif;font-size:16px}
.main-nav a{display:block;color:#555;text-decoration:none;padding:10px 19px;height:58px}
.main-nav a.active{background:var(--sky);color:var(--white);border-radius:2px 2px 0 0}

/* hero */
.hero{position:absolute;top:84px;left:0;width:966px;height:412px;background:linear-gradient(var(--sky) 0%,var(--sky) 80%,var(--sky-light) 100%)}
.hero-title{position:absolute;left:35px;top:43px;font-family:"Roboto Condensed",sans-serif;font-weight:700;font-size:35px;color:#2f3a40}
.hero-points{position:absolute;left:38px;top:96px;list-style:none;font-family:"Roboto Condensed",sans-serif;font-size:16px;color:#2a4a5a}
.hero-points li{display:flex;align-items:center;gap:8px;height:29px}
.hero-quote{position:absolute;left:40px;top:170px;width:520px;font-size:11.4px;line-height:17.5px;color:var(--white);padding-left:25px}
.quote-mark{position:absolute;font-family:Georgia,serif;font-size:44px;color:#1f7fb0;line-height:1}
.quote-open{left:0;top:-6px}
.quote-close{position:static;font-size:30px;vertical-align:-14px}
.hero-actions{position:absolute;left:199px;top:270px;display:flex;gap:13px}
.btn{display:block;font-family:"Roboto Condensed",sans-serif;font-weight:700;font-size:17px;color:#1f3d08;text-decoration:none;background:linear-gradient(#7fd82c,var(--green));border-bottom:3px solid var(--green-dark);padding:10px 18px;border-radius:2px}
.hero-visual{position:absolute;left:638px;top:44px;width:284px;height:287px;background:linear-gradient(135deg,#48c8f5,#0a8fcc);border:1px solid #7fd6f7;box-shadow:0 4px 12px rgba(0,0,0,.25)}
.slide-dots{position:absolute;left:435px;top:361px;display:flex;gap:10px}
.slide-dots span{width:12px;height:12px;background:#3b4a52;border:1px solid #20292e}
.slide-dots span.on{background:var(--sky-deep);border-color:#066}

/* content card */
.content{position:absolute;left:10px;top:471px;width:946px;height:481px;background:var(--white);border-radius:4px 4px 0 0}
.section-title{font-family:"Roboto Condensed",sans-serif;font-weight:700;font-size:23px;color:var(--ink);padding-bottom:6px;border-bottom:1px dashed #999;display:inline-block}
.section-title .accent{color:var(--sky)}
.welcome{position:absolute;left:14px;top:24px;width:646px}
.welcome .section-title{padding-right:40px}
.welcome p{font-size:11.2px;line-height:17.5px;color:var(--muted);margin-top:8px}
.welcome p + p{margin-top:6px}
.news{position:absolute;left:666px;top:25px;width:266px;height:181px;border:1px solid #ccc}
.news-head{background:var(--panel-dark);color:var(--white);font-family:"Roboto Condensed",sans-serif;font-weight:700;font-size:17px;height:36px;line-height:36px;padding-left:10px}
.news-item{margin:0 10px;padding:9px 0 7px;border-bottom:1px solid #ddd}
.news-item:last-child{border-bottom:0}
.news-item time{font-size:11.5px;font-weight:700;color:#333}
.news-item p{font-size:11px;line-height:17.5px;color:var(--muted);text-align:justify;margin-top:3px}
.features-title{position:absolute;left:14px;top:230px}
.features-title .section-title{padding-right:30px}
.features{position:absolute;left:29px;top:269px;display:flex;gap:39px}
.feature{width:193px;height:193px;border-radius:50%;background:radial-gradient(circle at 50% 40%,#f7f7f7,var(--circle));border:1px solid #ddd;box-shadow:2px 3px 0 #ccc;text-align:center;position:relative}
.feature-icon{position:absolute;left:66px;top:18px;width:62px;height:62px;border-radius:50%;background:linear-gradient(#bbb,#777)}
.feature-name{position:absolute;left:0;right:0;top:106px;font-family:"Roboto Condensed",sans-serif;font-weight:700;font-size:25px;line-height:26px;color:#6a6a6a}

/* footer widgets */
.widgets{position:absolute;left:0;top:952px;width:966px;height:201px;background:var(--footer)}
.widget{position:absolute;top:0;width:290px;height:180px;background:var(--footer-panel);border:1px solid var(--footer-line);border-top:0;padding:16px 13px}
.widget h3{font-family:"Roboto Condensed",sans-serif;font-weight:400;font-size:18px;color:#ddd;padding-bottom:7px;border-bottom:1px solid #444;width:160px}
.widget-icon{position:absolute;right:12px;top:10px}
.widget p{font-size:11px;line-height:17.5px;color:#aaa;margin-top:10px}
.widget .link{color:var(--sky)}
.widget-blog{left:29px}
.widget-updates{left:338px}
.widget-subscribe{left:647px}
.subscribe-form{display:flex;margin-top:14px;border:3px solid #3a3a3a;border-radius:3px;background:#3a3a3a}
.subscribe-form span{flex:1;height:28px;background:linear-gradient(#ccc,#e6e6e6)}
.subscribe-form b{width:94px;height:28px;background:var(--sky-deep);color:var(--white);font-family:"Roboto Condensed",sans-serif;font-size:16px;line-height:28px;text-align:center}
.widget-subscribe p{margin-top:8px}
.site-footer{position:absolute;left:0;top:1153px;width:966px;height:47px;background:#111;color:#bbb;font-size:11.5px;text-align:center;line-height:47px}
</style>
</head>
<body>
<div class="page">
  <header class="site-header">
    <div class="brand"><span class="brand-mark"></span><span class="brand-name">resale bright</span></div>
    <nav class="main-nav">
      <a class="active" href="#">Home</a><a href="#">About Us</a><a href="#">Customers</a><a href="#">Pricing</a><a href="#">Solutions</a><a href="#">Contact Us</a>
    </nav>
  </header>

  <section class="hero">
    <h1 class="hero-title">The Online Point-of Sale Solution</h1>
    <ul class="hero-points">
      <li><svg width="24" height="20" viewBox="0 0 24 20"><path d="M2 10l7 7L22 2" fill="none" stroke="#5fbf16" stroke-width="4" stroke-linecap="round" stroke-linejoin="round"/></svg>There are many variations of passages of Lorem Ipsum available, but the majority have</li>
      <li><svg width="24" height="20" viewBox="0 0 24 20"><path d="M2 10l7 7L22 2" fill="none" stroke="#5fbf16" stroke-width="4" stroke-linecap="round" stroke-linejoin="round"/></svg>Suffered alteration in some form, by injected humour.</li>
    </ul>
    <blockquote class="hero-quote">
      <span class="quote-mark quote-open">&ldquo;</span>
      Lorem Ipsum is simply dummy text of the printing and typesetting industry. Lorem Ipsum has been the industry's standard dummy text ever since the 1500s, when an unknown printer took a galley of type and scrambled it to make a type specimen book. It has survived not only five centuries, but also the leap into electronic typesetting, <span class="quote-mark quote-close">&rdquo;</span>
    </blockquote>
    <div class="hero-actions"><a class="btn" href="#">Start for trial</a><a class="btn" href="#">Demo</a></div>
    <div class="hero-visual" role="img" aria-label="Diagram of SaaS at the centre, surrounded by Network, Application, Helpdesk and SLA"></div>
    <div class="slide-dots"><span class="on"></span><span></span><span></span><span></span><span></span></div>
  </section>

  <main class="content">
    <section class="welcome">
      <h2 class="section-title">Welcome to <span class="accent">RESALE BRIGHT</span></h2>
      <p>Lorem Ipsum is simply dummy text of the printing and typesetting industry. Lorem Ipsum has been the industry's standard dummy text ever since the 1500s, when an unknown printer took a galley of type and scrambled it to make a type specimen book. It has survived not only five centuries, but also the leap into electronic typesetting, remaining essentially unchanged.</p>
      <p>It is a long established fact that a reader will be distracted by the readable content of a page when looking at its layout. The point of using Lorem Ipsum is that it has a more-or-less normal distribution of letters, as opposed to using 'Content here, content here', making it look like readable English. Many desktop publishing packages and web page editors now use Lorem Ipsum as their default model text.</p>
    </section>
    <aside class="news">
      <div class="news-head">Latest News</div>
      <article class="news-item"><time>September 1, 2012</time><p>Lorem Ipsum is simply dummy text of the printing and typesetting industry.</p></article>
      <article class="news-item"><time>September 1, 2012</time><p>Lorem Ipsum is simply dummy text of the printing and typesetting industry.</p></article>
    </aside>
    <div class="features-title"><h2 class="section-title">Lorem Ipsum is simply dummy text</h2></div>
    <div class="features">
      <div class="feature"><div class="feature-icon" role="img" aria-label="Gear icon"></div><div class="feature-name">Pre-Built<br>Applications</div></div>
      <div class="feature"><div class="feature-icon" role="img" aria-label="Gear icon"></div><div class="feature-name">Pre-Built<br>Applications</div></div>
      <div class="feature"><div class="feature-icon" role="img" aria-label="Gear icon"></div><div class="feature-name">Pre-Built<br>Applications</div></div>
      <div class="feature"><div class="feature-icon" role="img" aria-label="Gear icon"></div><div class="feature-name">Pre-Built<br>Applications</div></div>
    </div>
  </main>

  <section class="widgets">
    <div class="widget widget-blog">
      <h3>Recent Blog Posts</h3>
      <svg class="widget-icon" width="34" height="34" viewBox="0 0 34 34"><path d="M6 28l2-8L24 4l6 6-16 16z" fill="#777"/><path d="M6 28l2-8 6 6z" fill="#999"/></svg>
      <p><span class="link">9/1/2012</span><br>Lorem Ipsum is simply dummy text of the printing and typesetting industry.</p>
    </div>
    <div class="widget widget-updates">
      <h3>Recent Zentiq</h3>
      <p><span class="link">about 8 hours ago</span> Lorem Ipsum is simply dummy text of the printing and typesetting industry. Lorem Ipsum has been the industry's standard dummy text ever since the 1500s, when an unknown printer took a galley of type and scrambled.<br><span class="link">There are many</span></p>
    </div>
    <div class="widget widget-subscribe">
      <h3>Subscribe to Updates</h3>
      <svg class="widget-icon" width="40" height="34" viewBox="0 0 40 34"><path d="M2 14L20 2l18 12v18H2z" fill="#777"/><path d="M2 14l18 11 18-11" fill="none" stroke="#444" stroke-width="2"/><rect x="11" y="10" width="18" height="2" fill="#444"/></svg>
      <div class="subscribe-form"><span></span><b>Subscribe</b></div>
      <p>Lorem Ipsum is simply dummy text of the printing and typesetting industry. Lorem Ipsum has been the industry's standard dummy text ever since the 1500s,</p>
    </div>
  </section>

  <footer class="site-footer">Copyright @ 2012, Resale Bright. All Rights Reserved</footer>
</div>
</body>
</html>
```